wealth management firm, professional group, new model

we have a logo that works but we need a card, white background using our colors...clean look

our tag line if can be used in

The Bridge From Client to Owner

```html
<!DOCTYPE html>
<html lang="en">
<head>
<meta charset="UTF-8">
<title>Arcova Wealth Partners – Business Card</title>
<link href="https://fonts.googleapis.com/css2?family=Montserrat:wght@400;600&display=swap" rel="stylesheet">
<style>
  :root {
    --backdrop: #2a2a2a;
    --card: #ffffff;
    --card-shade: #ececec;
    --navy: #1b2a4a;
    --grey-text: #6b6f78;
    --rule: #8fa2c4;
  }
  * { margin: 0; padding: 0; box-sizing: border-box; }
  html, body {
    width: 1200px; height: 900px; overflow: hidden;
    background: var(--backdrop);
    font-family: "Montserrat", sans-serif;
  }
  .stage {
    position: relative; width: 1200px; height: 900px;
    display: flex; flex-direction: column; align-items: center; justify-content: center; gap: 48px;
  }
  .card {
    position: relative; width: 640px; height: 366px;
    border-radius: 28px;
    background: linear-gradient(120deg, var(--card-shade) 0%, var(--card) 55%, var(--card) 100%);
    box-shadow: 0 18px 40px rgba(0,0,0,0.45);
    overflow: hidden;
  }
  .brand {
    position: absolute; right: 56px; top: 88px;
    display: flex; align-items: center; gap: 10px;
    color: var(--navy); font-weight: 400; font-size: 22px; line-height: 1;
    white-space: nowrap;
  }
  .brand-dot {
    width: 14px; height: 14px; border-radius: 50%;
    background: var(--navy); flex: none;
  }
  .contact {
    position: absolute; left: 56px; top: 168px; color: var(--grey-text); font-size: 14px;
  }
  .contact-name { color: var(--navy); font-weight: 600; font-size: 18px; letter-spacing: 0.5px; line-height: 1.2; }
  .contact-role { margin-top: 2px; }
  .divider { width: 34px; height: 1.5px; background: var(--rule); margin: 9px 0; }
  .address { line-height: 1.35; }
  .lines { list-style: none; margin-top: 6px; }
  .lines li { display: flex; align-items: center; gap: 8px; margin-bottom: 5px; }
  .lines svg { width: 14px; height: 14px; fill: none; stroke: var(--navy); stroke-width: 1.6; flex: none; }
  .lines b { color: var(--navy); font-weight: 600; }
</style>
</head>
<body>
<main class="stage">
  <section class="card card-front">
    <div class="brand">
      <span class="brand-dot"></span>
      <span class="brand-name">Arcova Wealth Partners</span>
    </div>
  </section>

  <section class="card card-back">
    <div class="brand">
      <span class="brand-dot"></span>
      <span class="brand-name">Arcova Wealth Partners</span>
    </div>
    <div class="contact">
      <div class="contact-name">DANIEL REYES</div>
      <div class="contact-role">Director</div>
      <div class="divider"></div>
      <div class="address">00 dummy city<br>dummy place 0000</div>
      <div class="divider"></div>
      <ul class="lines">
        <li>
          <svg viewBox="0 0 16 16"><path d="M3 2h3l1.5 3.5-2 1.2a8 8 0 0 0 3.8 3.8l1.2-2L14 10v3a1 1 0 0 1-1 1A11 11 0 0 1 2 3a1 1 0 0 1 1-1z"/></svg>
          <span>555-014-2290</span>
        </li>
        <li>
          <svg viewBox="0 0 16 16"><rect x="1.5" y="3.5" width="13" height="9" rx="1"/><path d="M1.5 4l6.5 5 6.5-5"/></svg>
          <span>info@<b>arcovawealth</b>.com</span>
        </li>
        <li>
          <svg viewBox="0 0 16 16"><circle cx="8" cy="8" r="6.5"/><path d="M1.5 8h13M8 1.5c-3 3.5-3 9.5 0 13M8 1.5c3 3.5 3 9.5 0 13"/></svg>
          <span>www.<b>arcovawealth</b>.com</span>
        </li>
      </ul>
    </div>
  </section>
</main>
</body>
</html>
```